We sell companies excess stock for them

We need a business card for a company based in New Zealand called 'StockHarbor'.

Check out our website to get an idea www.stockharbor.example

We help other businesses to;
- Sell Excess Stock
- Manage Product Returns
- Sell Company Assets

Our logo is attached for your reference
The font used is 'RifficFree-Bold'

Target Market(s)

Businesses

Industry/Entity Type

Business

Contact Information for Business Card

Name: Mark Pellow
Phone: 027 846 2093
email: markpellow@stockharbor.example
website: www.stockharbor.example

Font styles to use
Other font styles liked:
• Unsure

Colors
9bcb3b

Requirements
Must have
• coming soon
Nice to have
• coming soon
Should not have
• coming soon

```html
<!DOCTYPE html>
<html lang="en">
<head>
<meta charset="utf-8">
<title>StockHarbor Business Card</title>
<link href="https://fonts.googleapis.com/css2?family=Fredoka:wght@600;700&family=Lato:wght@400;700&display=swap" rel="stylesheet">
<style>
  :root {
    --bg: #1c1c1c;
    --card: #252525;
    --card-edge: #2e2e2e;
    --green: #9bcb3b;
    --white: #f4f4f4;
    --grey: #8a8a8a;
    --mascot-green: #7fbf3a;
    --mascot-orange: #f0a030;
  }
  * { box-sizing: border-box; margin: 0; padding: 0; }
  html, body { width: 1200px; height: 900px; overflow: hidden; background: var(--bg); }
  .canvas { position: relative; width: 1200px; height: 900px; }
  .card {
    position: absolute; left: 250px; width: 700px; height: 400px;
    background: linear-gradient(160deg, var(--card-edge), var(--card));
    box-shadow: 0 10px 30px rgba(0,0,0,.6);
  }
  .card--back { top: 35px; }
  .card--front { top: 465px; }

  .back-content { position: absolute; inset: 0; display: flex; flex-direction: column; align-items: center; justify-content: center; text-align: center; }
  .back-wordmark { font-family: "Fredoka", sans-serif; font-weight: 700; font-size: 96px; color: var(--grey); letter-spacing: -1px; line-height: 1; margin-bottom: 34px; }
  .back-lead { font-family: "Fredoka", sans-serif; font-weight: 700; font-size: 22px; color: var(--green); margin-bottom: 6px; }
  .back-services { font-family: "Lato", sans-serif; font-size: 21px; color: var(--white); line-height: 1.35; letter-spacing: .5px; }

  .mascot { position: absolute; left: 70px; top: 100px; width: 190px; height: 220px; border-radius: 40% 40% 30% 30%;
    background: radial-gradient(circle at 45% 40%, var(--mascot-orange) 0 20%, var(--mascot-green) 45%, #3d6b1e 80%, transparent 81%); }
  .divider { position: absolute; left: 300px; top: 130px; width: 3px; height: 190px; background: var(--green); }
  .details { position: absolute; left: 340px; top: 120px; }
  .wordmark { font-family: "Fredoka", sans-serif; font-weight: 700; font-size: 54px; color: var(--white); line-height: 1; margin-bottom: 20px; }
  .person { font-family: "Fredoka", sans-serif; font-weight: 700; font-size: 32px; color: var(--white); text-transform: uppercase; line-height: 1; }
  .person .surname { color: var(--green); }
  .role { font-family: "Lato", sans-serif; font-size: 20px; color: var(--white); margin: 4px 0 18px; }
  .contacts { list-style: none; font-family: "Lato", sans-serif; font-size: 19px; color: var(--white); }
  .contacts li { display: flex; align-items: center; gap: 12px; margin-bottom: 4px; }
  .contacts svg { width: 16px; height: 16px; fill: var(--green); flex: none; }
  .accent { color: var(--green); }
</style>
</head>
<body>
<main class="canvas">
  <section class="card card--back" aria-label="Card back">
    <div class="back-content">
      <div class="back-wordmark">StockHarbor</div>
      <p class="back-lead">We help other businesses to:</p>
      <p class="back-services">Sell Excess Stock | Manage Product Returns<br>Sell Company Assets</p>
    </div>
  </section>

  <section class="card card--front" aria-label="Card front">
    <div class="mascot" role="img" aria-label="Cartoon courier mascot in green overalls carrying an orange parcel"></div>
    <div class="divider"></div>
    <div class="details">
      <div class="wordmark">StockHarbor</div>
      <div class="person">Mark <span class="surname">Pellow</span></div>
      <div class="role">Director</div>
      <ul class="contacts">
        <li><svg viewBox="0 0 16 16"><path d="M3 1l3 3-1.5 2a9 9 0 0 0 5.5 5.5L12 10l3 3-2 2C7 15 1 9 1 3z"/></svg>027 846 2093</li>
        <li><svg viewBox="0 0 16 16"><path d="M1 3h14v10H1z M1 3l7 6 7-6" fill="none" stroke="#9bcb3b" stroke-width="1.6"/></svg>markpellow@stockharbor.example</li>
        <li><svg viewBox="0 0 16 16"><g fill="none" stroke="#9bcb3b" stroke-width="1.4"><circle cx="8" cy="8" r="6.5"/><ellipse cx="8" cy="8" rx="3" ry="6.5"/><path d="M1.5 8h13"/></g></svg>www.<span class="accent">stockharbor</span>.example</li>
      </ul>
    </div>
  </section>
</main>
</body>
</html>
```